Income Tax and Accounting Brochure

I need a brochure using my new logo (file attached). I do tax work and accounting work. I am an EA (QDX Enrolled Agent - logo attached) and would like this incorporated into the brochure. I also have a MSA in Accounting. Please incorporate the text that I have provided in the brochure.

Target Market(s)

Tax Clients - both business and individuals

Industry/Entity Type

Accounting

Colors
0054AA
0677BA
7BADD7
CADEEF
E8F1F8

Requirements
Must have
• Use my logo and the QDX EA file in the brochure
Nice to have
• I would like to see a brochure that I can customize with my own text if possible.

```html
<!DOCTYPE html>
<html lang="en">
<head>
<meta charset="utf-8">
<title>Harbor Ledger – Income Tax and Accounting Brochure</title>
<link rel="stylesheet" href="https://fonts.googleapis.com/css2?family=Lato:wght@400;700;900&family=Montserrat:wght@400;500;600&display=swap">
<style>
:root{
  --stage:#d3eeef;
  --brand-blue:#1f4fa3;
  --brand-red:#c11f33;
  --ink:#1a1a1a;
  --body:#3f3f3f;
  --paper:#ffffff;
}
*{margin:0;padding:0;box-sizing:border-box}
html,body{width:894px;height:1200px;overflow:hidden;background:var(--stage)}
body{position:relative;font-family:"Montserrat",sans-serif;color:var(--body)}
.spread{position:absolute;left:97px;width:700px;height:495px;background:var(--paper);overflow:hidden;box-shadow:0 2px 6px rgba(0,0,0,.12)}
.spread--outer{top:80px}
.spread--inner{top:626px}
.shapes{position:absolute;left:0;top:0;width:700px;height:495px}
.abs{position:absolute}
.photo{position:absolute;border-radius:50%;border:4px solid var(--paper)}
.headline{font-family:"Lato",sans-serif;font-weight:900;color:var(--ink);line-height:1}
.accent{color:var(--brand-red)}
.body-copy{font-size:7px;line-height:13.5px;color:var(--body)}
.section-title{font-family:"Lato",sans-serif;font-weight:700;font-size:12px;color:var(--ink)}
.rule{position:absolute;height:1.5px;background:var(--brand-red)}
.contact-list{list-style:none;width:260px;height:110px}
.contact-item{position:absolute;left:0;width:260px;display:flex;align-items:flex-start;gap:7px;font-size:6.6px;line-height:9px;color:var(--ink);white-space:nowrap}
.contact-icon{width:17px;height:17px;flex:none;margin-top:-1px}
.brand-lockup{display:flex;align-items:center;gap:6px}
.brand-name{font-family:"Montserrat",sans-serif;font-weight:600;font-size:8px;line-height:10px;color:var(--brand-blue);letter-spacing:.4px}
.benefit{position:absolute;display:flex;gap:8px;width:150px;font-size:5.9px;line-height:10px;color:var(--body)}
.benefit svg{width:26px;height:26px;flex:none}
.footer-contact{position:absolute;left:176px;width:170px;display:flex;gap:7px;align-items:flex-start;font-size:5.8px;line-height:8.5px;color:#fff;white-space:nowrap}
.footer-contact svg{width:11px;height:11px;flex:none}
</style>
</head>
<body>

<section class="spread spread--outer">
  <svg class="shapes" viewBox="0 0 700 495">
    <path d="M0 245 C20 300 60 322 135 326 L170 495 L0 495 Z" fill="var(--brand-blue)"/>
    <path d="M255 0 Q342 12 351 88 Q362 18 445 0 Z" fill="var(--brand-red)"/>
    <path d="M380 60 A158 158 0 0 0 560 306 A170 170 0 0 1 380 60 Z" fill="var(--brand-blue)"/>
    <path d="M555 326 Q650 318 700 255 L700 268 Q660 318 555 326 Z" fill="var(--brand-red)"/>
    <path d="M351 456 Q520 450 700 466 L700 495 L351 495 Z" fill="var(--brand-blue)"/>
  </svg>

  <h1 class="headline abs" style="left:20px;top:24px;font-size:25px;letter-spacing:.6px">BOOKS A MESS:</h1>
  <p class="headline abs accent" style="left:20px;top:52px;font-size:18px;font-weight:700">NO PROBLEM!</p>
  <p class="body-copy abs" style="left:20px;top:83px;width:312px">If you own a small business and haven't kept up your bookkeeping, don't worry. We can help you. We'll prepare your bookkeeping for the year, prepare a full Schedule C, as well as your personal income tax return. Then we'll help you set up an easy system that allows you to keep your books in tip-top shape next year.</p>

  <h2 class="section-title abs" style="left:20px;top:161px">Get In Touch With Us:</h2>
  <div class="rule" style="left:20px;top:177px;width:46px"></div>

  <div class="abs" style="left:226px;top:163px;width:103px;height:26px;border:2px solid #b09a63;background:#eef1f3" role="img" aria-label="Enrolled agent certification badge"></div>

  <ul class="contact-list abs" style="left:34px;top:190px">
    <li class="contact-item" style="top:0">
      <svg class="contact-icon" viewBox="0 0 18 18"><path d="M9 1 A8 8 0 0 0 9 17" fill="none" stroke="var(--brand-blue)" stroke-width="1.3"/><path d="M10 4.5a3 3 0 0 0-3 3c0 2.2 3 5.5 3 5.5s3-3.3 3-5.5a3 3 0 0 0-3-3z" fill="var(--brand-red)"/><circle cx="10" cy="7.5" r="1" fill="#fff"/></svg>
      <span>123 Sample Street, New City,<br>NY-654</span>
    </li>
    <li class="contact-item" style="top:27px">
      <svg class="contact-icon" viewBox="0 0 18 18"><path d="M9 1 A8 8 0 0 0 9 17" fill="none" stroke="var(--brand-blue)" stroke-width="1.3"/><path d="M7.5 5l1.6-.3 1 2-1 .9a5 5 0 0 0 2.3 2.3l.9-1 2 1-.3 1.6c-3.5.3-6.8-3-6.5-6.5z" fill="var(--brand-red)"/></svg>
      <span>Call Us:<br>(+1) 123 456 7890</span>
    </li>
    <li class="contact-item" style="top:54px">
      <svg class="contact-icon" viewBox="0 0 18 18"><path d="M9 1 A8 8 0 0 0 9 17" fill="none" stroke="var(--brand-blue)" stroke-width="1.3"/><rect x="6" y="6" width="8" height="6" fill="var(--brand-red)"/><path d="M6 6l4 3.2L14 6" fill="none" stroke="#fff" stroke-width=".7"/></svg>
      <span>Email Us:<br>info@harborledgerconsulting.com</span>
    </li>
    <li class="contact-item" style="top:82px">
      <svg class="contact-icon" viewBox="0 0 18 18"><path d="M9 1 A8 8 0 0 0 9 17" fill="none" stroke="var(--brand-blue)" stroke-width="1.3"/><circle cx="10" cy="9" r="3.6" fill="var(--brand-red)"/><path d="M6.4 9h7.2M10 5.4v7.2" stroke="#fff" stroke-width=".5"/></svg>
      <span>Visit Us:<br>www.harborledgerconsulting.com</span>
    </li>
  </ul>

  <div class="photo" role="img" aria-label="Photo of two people shaking hands over a desk with a calculator and papers" style="left:84px;top:302px;width:230px;height:230px;background:radial-gradient(circle at 60% 25%,#f2c27a 0%,#c9a27a 30%,#8a8278 60%,#d9d9d6 100%)"></div>

  <div class="photo" role="img" aria-label="Photo of two businessmen shaking hands in a bright office" style="left:397px;top:-8px;width:312px;height:312px;border:none;background:linear-gradient(135deg,#c6ccd4 0%,#8a939f 40%,#6f87a8 70%,#b9c7d8 100%)"></div>

  <div class="brand-lockup abs" style="left:370px;top:325px">
    <span style="width:27px;height:27px;border-radius:50%;background:var(--brand-blue);display:block"></span>
    <span class="brand-name">HARBOR LEDGER<br>ACCOUNTING &amp; CONSULTING, LLC</span>
  </div>

  <h2 class="headline abs" style="left:370px;top:372px;font-size:28.5px">INCOME TAX</h2>
  <div class="rule" style="left:370px;top:398px;width:262px;height:1px"></div>
  <h2 class="headline abs" style="left:370px;top:402px;font-size:28.5px">AND ACCOUNTING</h2>

  <div class="abs" style="left:370px;top:464px;display:flex;align-items:center;gap:7px;color:#fff;font-size:8.5px">
    <svg width="17" height="17" viewBox="0 0 18 18"><path d="M9 1 A8 8 0 0 0 9 17" fill="none" stroke="#fff" stroke-width="1.3"/><circle cx="10" cy="9" r="3.6" fill="#fff"/><path d="M6.4 9h7.2M10 5.4v7.2" stroke="var(--brand-blue)" stroke-width=".5"/></svg>
    <span>www. harborledger.com</span>
  </div>
</section>

<section class="spread spread--inner">
  <svg class="shapes" viewBox="0 0 700 495">
    <path d="M0 0 L55 0 Q10 5 0 45 Z" fill="var(--brand-red)"/>
    <path d="M645 0 L700 0 L700 45 Q692 5 645 0 Z" fill="var(--brand-red)"/>
    <path d="M0 370 Q80 315 175 322 Q270 332 351 358 L351 495 L0 495 Z" fill="var(--brand-red)"/>
    <path d="M0 385 Q90 325 190 333 Q290 345 380 380 Q450 400 510 378 Q600 352 700 378 L700 495 L0 495 Z" fill="var(--brand-blue)"/>
  </svg>

  <h1 class="headline abs" style="left:21px;top:23px;font-size:26px;letter-spacing:-.3px">ABOUT <span class="accent">MARLENE D</span></h1>
  <p class="headline abs" style="left:21px;top:49px;font-size:26px;letter-spacing:-.3px"><span class="accent">OKAFOR</span>, <span style="font-weight:400;font-size:16px;letter-spacing:.5px">MSA EA (PRINCIPAL)</span></p>
  <p class="body-copy abs" style="left:20px;top:83px;width:305px">I have a Masters' Degree in accounting and am an QDX Enrolled Agent. I am also a LedgerBooks Advanced Certified Consultant in both the online and desktop products including Enterprise and Point of Sale. I provide individual and small business tax services, Accounting, bookkeeping, QDX representation, insurance audit representation, business license assistance and more.</p>

  <div class="abs" role="img" aria-label="Photo of a smiling man in a dark suit pointing toward the quote" style="left:17px;top:161px;width:150px;height:193px;border-radius:60px 60px 0 0;background:linear-gradient(180deg,#e9e4df 0%,#c9b9aa 25%,#2d3038 45%,#1d2028 100%)"></div>

  <p class="abs" style="left:177px;top:181px;font-family:'Lato',sans-serif;font-weight:900;font-size:24px;color:var(--brand-blue);line-height:1">&ldquo;</p>
  <p class="abs" style="left:177px;top:196px;width:148px;font-size:7px;line-height:14.5px;text-align:justify;color:var(--body)"><span style="display:inline-block;width:32px"></span>I have experience working with a wide variety of clients from the point where they first decide they want to start a business. They are often unsure about what to do first- I have a lot of experience to offer you.&rdquo;</p>

  <div class="abs" style="left:44px;top:407px;display:flex;flex-direction:column;align-items:center;gap:4px">
    <span style="width:50px;height:50px;border-radius:50%;border:3px solid #fff;display:block"></span>
    <span style="font-family:'Montserrat',sans-serif;font-weight:600;font-size:7px;color:#fff;letter-spacing:.4px">HARBOR LEDGER</span>
  </div>

  <h3 class="abs" style="left:176px;top:376px;font-family:'Montserrat',sans-serif;font-weight:600;font-size:9.5px;color:#fff">GET IN TOUCH</h3>
  <div class="abs" style="left:176px;top:392px;width:24px;height:1.5px;background:#fff"></div>
  <div class="footer-contact" style="top:402px">
    <svg viewBox="0 0 12 12"><path d="M6 1a3.5 3.5 0 0 0-3.5 3.5C2.5 7 6 11 6 11s3.5-4 3.5-6.5A3.5 3.5 0 0 0 6 1z" fill="none" stroke="#fff" stroke-width=".7"/><circle cx="6" cy="4.5" r="1.2" fill="none" stroke="#fff" stroke-width=".7"/></svg>
    <span>123 Sample Street, New City,<br>NY-654</span>
  </div>
  <div class="footer-contact" style="top:427px">
    <svg viewBox="0 0 12 12"><path d="M2 2l2.2-.5 1.3 2.6-1.2 1a6 6 0 0 0 2.6 2.6l1-1.2 2.6 1.3L10 10C5.5 10.3 1.7 6.5 2 2z" fill="none" stroke="#fff" stroke-width=".7"/></svg>
    <span>(+1) 123 456 7890</span>
  </div>
  <div class="footer-contact" style="top:447px">
    <svg viewBox="0 0 12 12"><rect x="1.5" y="3" width="9" height="6.5" fill="none" stroke="#fff" stroke-width=".7"/><path d="M1.5 3L6 6.8 10.5 3" fill="none" stroke="#fff" stroke-width=".7"/></svg>
    <span>info@harborledgerconsulting.com</span>
  </div>
  <div class="footer-contact" style="top:467px">
    <svg viewBox="0 0 12 12"><circle cx="6" cy="6" r="4.5" fill="none" stroke="#fff" stroke-width=".7"/><path d="M1.5 6h9M6 1.5c-2 2.5-2 6.5 0 9M6 1.5c2 2.5 2 6.5 0 9" fill="none" stroke="#fff" stroke-width=".6"/></svg>
    <span>www.harborledgerconsulting.com</span>
  </div>

  <h2 class="headline abs" style="left:370px;top:25px;font-size:19.5px;line-height:23.5px;width:320px">WHAT A JOY IT IS TO <span class="accent">WATCH SUCCESS</span> IN ACTION!</h2>
  <p class="body-copy abs" style="left:370px;top:80px;width:312px">Preparing your own income tax return can be a task that leaves you with more questions than answers. According to a study released by the National Tax Review Office last year, most taxpayers (77% of 71 million taxpayers) believe they benefited from using a professional tax preparer.</p>
  <p class="body-copy abs" style="left:370px;top:141px;width:312px">Whether we like it or not, today's tax laws are so complicated that filing a relatively simple return can be confusing. It is just too easy to overlook deductions and credits to which you are entitled. Even if you use a computer software program there's no substitute for the assistance of an experienced tax professional.</p>

  <h3 class="abs" style="left:370px;top:208px;font-family:'Montserrat',sans-serif;font-weight:600;font-size:12px;color:var(--brand-blue)">Here's what your get...</h3>
  <div class="rule" style="left:370px;top:228px;width:46px"></div>

  <div class="benefit" style="left:370px;top:242px">
    <svg viewBox="0 0 26 26"><path d="M13 1 A12 12 0 0 0 13 25" fill="none" stroke="var(--brand-blue)" stroke-width="1.3"/><rect x="9" y="7" width="10" height="12" fill="none" stroke="var(--brand-red)" stroke-width=".9"/><path d="M11 10h6M11 13h6M11 16h4" stroke="var(--brand-red)" stroke-width=".8"/></svg>
    <span>Your tax return will be checked and rechecked by our computer software identifying potential problems the QDX may look at more closely &amp; reviewing the math to limit QDX contacts.</span>
  </div>
  <div class="benefit" style="left:527px;top:242px">
    <svg viewBox="0 0 26 26"><path d="M13 1 A12 12 0 0 0 13 25" fill="none" stroke="var(--brand-blue)" stroke-width="1.3"/><rect x="9" y="7" width="10" height="12" fill="none" stroke="var(--brand-red)" stroke-width=".9"/><path d="M11 10h6M11 13h6M11 16h4" stroke="var(--brand-red)" stroke-width=".8"/></svg>
    <span>Our staff will show you how to adjust your payroll withholding to get more money back each week. Why give the QDX an interest free loan for up to 16 months.</span>
  </div>
  <div class="benefit" style="left:370px;top:306px">
    <svg viewBox="0 0 26 26"><path d="M13 1 A12 12 0 0 0 13 25" fill="none" stroke="var(--brand-blue)" stroke-width="1.3"/><rect x="9" y="7" width="10" height="12" fill="none" stroke="var(--brand-red)" stroke-width=".9"/><path d="M11 10h6M11 13h6M11 16h4" stroke="var(--brand-red)" stroke-width=".8"/></svg>
    <span>Your tax return can be filed electronically so you will get a refund back quicker.</span>
  </div>
  <div class="benefit" style="left:527px;top:304px">
    <svg viewBox="0 0 26 26"><path d="M13 1 A12 12 0 0 0 13 25" fill="none" stroke="var(--brand-blue)" stroke-width="1.3"/><rect x="9" y="7" width="10" height="12" fill="none" stroke="var(--brand-red)" stroke-width=".9"/><path d="M11 10h6M11 13h6M11 16h4" stroke="var(--brand-red)" stroke-width=".8"/></svg>
    <span>We will show you potential deductions to limit your tax liability for next year. In addition, we will give you a sheet of commonly overlooked deductions to limit the following year's tax liability.</span>
  </div>

  <div class="abs" style="left:405px;top:362px;width:238px;height:238px;border-radius:50%;background:var(--brand-red)"></div>
  <div class="photo" role="img" aria-label="Photo of a hand using a calculator at a desk beside a laptop" style="left:411px;top:372px;width:226px;height:226px;background:linear-gradient(160deg,#f1e6d4 0%,#d8cdbd 35%,#9c958c 65%,#e8e3dc 100%)"></div>
</section>

</body>
</html>
```